Design home page for brightvane.xyz

We’re seeking a sleek, lead-generation-focused single-page website for Brightvane.xyz that communicates our expertise in delivering high-intent leads to mid-sized businesses. The goal is to guide visitors toward scheduling a free consultation while emphasizing our performance-based approach and comprehensive service offerings.

Industry/Entity Type

BRIGHTVANE

Number of Pages Required

1 page

Font styles to use
Sans Serif

Requirements
Must have
• content from https://files.quorvalet.example/doc/7hTmwQRZa93KpLdVyxNe42UcBsFoGj8rYiMn5EkPtWz/view?tab=t.0
Nice to have
• color pallet from here https://files.quorvalet.example/doc/4pRkz-NWb62VxLeTyqJs8cHaDmFu3GiYoBnQ5tXeKv/view?tab=t.0

```html
<!DOCTYPE html>
<html lang="en">
<head>
<meta charset="utf-8">
<title>Brightvane.xyz — High-Intent Lead Generation</title>
<link rel="stylesheet" href="https://fonts.googleapis.com/css2?family=Montserrat:wght@400;500;600;700;800&display=swap">
<style>
:root{
  --green:#52ae4c;
  --green-dark:#469a42;
  --green-footer:#43a03e;
  --orange:#e9481c;
  --blue:#2c74f6;
  --yellow:#fbb34b;
  --ink:#222;
  --muted:#6b6b6b;
  --line:#d9d9d9;
  --white:#fff;
}
*{box-sizing:border-box;margin:0;padding:0}
html,body{width:1200px;height:4418px;overflow:hidden}
body{font-family:"Montserrat",sans-serif;color:var(--ink);background:var(--white);position:relative}
.abs{position:absolute}
.btn{position:absolute;display:flex;align-items:center;justify-content:center;background:var(--orange);color:#fff;font-weight:700;font-size:13px;letter-spacing:.3px;text-transform:uppercase;z-index:2}
.underline{position:absolute;height:2px;background:var(--green);width:96px}
.section-title{position:absolute;left:0;width:1200px;text-align:center;font-size:28px;font-weight:500}

/* hero */
.hero{position:absolute;left:0;top:0;width:1200px;height:603px;background:var(--green);overflow:hidden}
.hero-ground{position:absolute;left:0;top:509px;width:1200px;height:94px;background:var(--green-dark)}
.logo{position:absolute;left:50px;top:24px;color:#fff;font-size:25px;font-weight:800;letter-spacing:.5px}
.nav{position:absolute;top:30px;left:455px;color:#fff;font-size:13.5px;font-weight:500}
.nav span{position:absolute;white-space:nowrap}
.hero h1{position:absolute;left:140px;top:230px;width:560px;text-align:center;color:#fff;font-size:30px;line-height:40px;font-weight:800;z-index:2;white-space:nowrap}
.hero .sub{position:absolute;left:140px;top:324px;width:560px;text-align:center;color:#fff;font-size:17px;font-weight:600;z-index:2;white-space:nowrap}
.hero-art{position:absolute;left:705px;top:165px;width:495px;height:405px;border-radius:40px 0 0 40px;background:radial-gradient(circle at 40% 45%,#7cc873,#52ae4c 70%)}
.hero-leaves{position:absolute;top:420px;width:160px;height:90px;border-radius:80px 80px 0 0;background:linear-gradient(#4b9c46,#3f8d3b)}
.hero-cloud{position:absolute;left:85px;top:128px;width:210px;height:70px;border-radius:40px;background:#74c26b}

/* about */
.about-photos{left:94px;top:692px;width:468px;height:340px;background:linear-gradient(135deg,#cfcfcf,#8a8a8a)}
.about h2{position:absolute;left:627px;top:692px;font-size:28px;font-weight:500}
.about .lead{position:absolute;left:623px;top:768px;color:var(--green);font-size:14px;font-weight:600}
.about p.body{position:absolute;left:623px;width:440px;color:var(--muted);font-size:13.5px;line-height:27px}
.divider{position:absolute;left:120px;width:960px;height:1px;background:var(--line)}

/* services */
.services-intro{position:absolute;left:90px;top:1256px;width:1020px;text-align:center;color:var(--muted);font-size:13.5px;line-height:27px}
.card{position:absolute;top:1357px;width:360px;height:309px;border:1.5px solid var(--line);background:#fff}
.card h3{position:absolute;left:30px;top:52px;font-size:18px;line-height:27px;font-weight:600}
.card p{position:absolute;left:30px;top:130px;width:300px;color:var(--muted);font-size:12px;line-height:22.5px}
.card .btn{left:30px;top:244px;width:94px;height:28px;font-size:12px;font-weight:500;text-transform:none}
.card svg{position:absolute;right:38px;top:54px}

/* how it works */
.how{position:absolute;left:0;top:1733px;width:1200px;height:653px;background:var(--blue)}
.step-box{position:absolute;width:321px;height:101px;background:#fff}
.step-box h4{position:absolute;left:47px;top:20px;font-size:18px;font-weight:600}
.step-box p{position:absolute;left:47px;top:52px;width:265px;color:var(--muted);font-size:12px;line-height:17px}
.step-ring{position:absolute;width:160px;height:160px;border-radius:50%;background:conic-gradient(var(--yellow) 0 50%,#6fc266 50% 100%);display:flex;align-items:center;justify-content:center}
.step-ring .inner{width:136px;height:136px;border-radius:50%;background:#fff;display:flex;align-items:center;justify-content:center}
.step-num{position:absolute;width:30px;height:30px;border-radius:50%;background:#fff;display:flex;align-items:center;justify-content:center;font-size:15px;font-weight:600}

/* why */
.why-art{left:111px;top:2486px;width:369px;height:342px;border-radius:20px;background:linear-gradient(135deg,#dfe9ff,#a8d8a3)}
.why h2{position:absolute;left:641px;top:2442px;font-size:28px;font-weight:500}
.why-item{position:absolute;left:639px;width:446px;height:85px;border:1.5px solid var(--line);border-left:6px solid var(--yellow);background:#fff}
.why-item h4{position:absolute;left:24px;top:18px;font-size:14.5px;font-weight:600}
.why-item p{position:absolute;left:24px;top:46px;color:var(--muted);font-size:12px}
.why-item svg{position:absolute;left:-24px;top:34px}

/* testimonials */
.t-card{position:absolute;top:3140px;width:278px;height:283px;border:1.5px solid var(--line);background:#fff;text-align:center}
.t-avatar{position:absolute;top:-34px;left:99px;width:80px;height:80px;border:2px solid var(--green);background:linear-gradient(#d8eed5,#a9d5a3)}
.t-card p{position:absolute;left:22px;top:72px;width:234px;color:var(--muted);font-size:12px;line-height:22.5px}
.t-stars{position:absolute;left:0;top:172px;width:100%;color:var(--yellow);font-size:17px;letter-spacing:6px}
.t-name{position:absolute;left:0;top:206px;width:100%;color:var(--green);font-size:13.5px;font-weight:600}
.t-role{position:absolute;left:0;top:226px;width:100%;color:var(--muted);font-size:10.5px;font-style:italic;font-weight:600}

/* partners */
.partners{position:absolute;left:40px;top:3500px;width:1120px;height:70px;display:flex;justify-content:space-between;align-items:center}
.partners span{font-size:21px;font-weight:700;color:#333}

/* contact */
.contact{position:absolute;left:0;top:3617px;width:1200px;height:703px;background:var(--green);color:#fff}
.contact h2{position:absolute;left:0;top:50px;width:1200px;text-align:center;font-size:28px;font-weight:500}
.contact .intro{position:absolute;left:280px;top:130px;width:640px;text-align:center;font-size:12px;line-height:22px}
.field-label{position:absolute;left:285px;font-size:14px;font-weight:500}
.field{position:absolute;left:285px;width:623px;height:41px;border:1px solid #fff;background:var(--green)}
.contact .btn{left:285px;top:631px;width:138px;height:44px}

footer{position:absolute;left:0;top:4320px;width:1200px;height:98px;background:var(--green-footer);color:#fff}
footer .copy{position:absolute;left:67px;top:44px;font-size:11px}
.social{position:absolute;top:42px;width:22px;height:22px;border-radius:50%;background:#fff}
</style>
</head>
<body>

<header class="hero">
  <div class="hero-ground"></div>
  <div class="hero-cloud"></div>
  <div class="hero-leaves" style="left:0"></div>
  <div class="hero-leaves" style="left:560px;width:140px"></div>
  <div class="hero-art" role="img" aria-label="Illustration of a person with a megaphone running beside a large magnet attracting customer icons and stars"></div>
  <div class="logo">BRIGHTVANE</div>
  <nav class="nav">
    <span style="left:0">Home</span>
    <span style="left:68px">About Us</span>
    <span style="left:157px">Services</span>
    <span style="left:235px">How It Works</span>
    <span style="left:352px">Why Choose Us</span>
    <span style="left:491px">Testimonials</span>
    <span style="left:610px">Contact us</span>
  </nav>
  <h1>High-Intent Lead Generation<br>for Mid-Sized Businesses</h1>
  <div class="sub">Delivering results with a performance-based approach</div>
  <div class="btn" style="left:305px;top:367px;width:221px;height:41px">Get Free Consultation</div>
</header>

<section class="about">
  <div class="abs about-photos" role="img" aria-label="Black and white team portraits"></div>
  <h2>About us</h2>
  <div class="underline" style="left:627px;top:740px"></div>
  <div class="lead">Lorem ipsum dolor sit amet, consectetur adipiscing elit</div>
  <p class="body" style="top:801px">Lorem ipsum dolor sit amet, consectetur adipiscing elit, sed do eiusmod tempor incididunt ut labore et dolore magna aliqua. Quis ipsum suspendisse ultrices gravida.</p>
  <p class="body" style="top:899px">Lorem ipsum dolor sit amet, consectetur adipiscing elit, sed do eiusmod tempor incididunt ut labore et dolore magna aliqua. Quis ipsum suspendisse ultrices gravida.</p>
</section>

<div class="divider" style="top:1101px"></div>

<section class="services">
  <div class="section-title" style="top:1176px">Our Services</div>
  <p class="services-intro">Lorem ipsum dolor sit amet, consectetur adipiscing elit, sed do eiusmod tempor incididunt ut labore et dolore magna aliqua. Quis ipsum suspendisse ultrices gravida. Risus commodo viverra maecenas accumsan</p>

  <div class="card" style="left:36px">
    <h3>Targeted Lead<br>Generation</h3>
    <svg width="70" height="60" viewBox="0 0 70 60" fill="none" stroke="#222" stroke-width="2"><circle cx="14" cy="10" r="6"/><circle cx="35" cy="10" r="6"/><circle cx="56" cy="10" r="6"/><circle cx="34" cy="34" r="13" stroke="#2c74f6"/><line x1="44" y1="44" x2="56" y2="56"/><path d="M4 30c0-8 20-8 20 0M46 30c0-8 20-8 20 0" stroke="#52ae4c"/></svg>
    <p>Identify and connect with the right audience using advanced targeting techniques, ensuring your message reaches potential customers most likely to convert.</p>
    <div class="btn">More info</div>
  </div>
  <div class="card" style="left:420px">
    <h3>Campaign<br>management</h3>
    <svg width="94" height="56" viewBox="0 0 94 56" fill="none"><rect x="1" y="1" width="92" height="54" rx="3" stroke="#222" stroke-width="2"/><rect x="8" y="30" width="5" height="16" fill="#52ae4c"/><rect x="16" y="22" width="5" height="24" fill="#2c74f6"/><rect x="24" y="34" width="5" height="12" fill="#52ae4c"/><rect x="32" y="26" width="5" height="20" fill="#2c74f6"/><rect x="64" y="7" width="22" height="22" fill="#2c74f6"/><circle cx="75" cy="40" r="8" fill="#2c74f6"/></svg>
    <p>Optimize your marketing efforts with data-driven strategies, seamless execution, and continuous refinement to ensure maximum return on investment and campaign success.</p>
    <div class="btn">More info</div>
  </div>
  <div class="card" style="left:802px">
    <h3>Analytics and<br>reporting</h3>
    <svg width="94" height="56" viewBox="0 0 94 56" fill="none"><rect x="1" y="1" width="92" height="54" rx="3" stroke="#222" stroke-width="2"/><rect x="10" y="38" width="6" height="10" fill="#52ae4c"/><rect x="20" y="32" width="6" height="16" fill="#52ae4c"/><rect x="30" y="36" width="6" height="12" fill="#52ae4c"/><rect x="40" y="26" width="6" height="22" fill="#52ae4c"/><rect x="50" y="28" width="6" height="20" fill="#52ae4c"/><rect x="60" y="18" width="6" height="30" fill="#52ae4c"/><polyline points="10,32 30,24 44,20 60,12 80,8" stroke="#2c74f6" stroke-width="3"/><path d="M74 6l8 2-4 7" stroke="#2c74f6" stroke-width="3"/></svg>
    <p>Transform data into actionable insights with detailed analytics and reporting, enabling informed decisions to drive growth, optimize performance, and achieve goals.</p>
    <div class="btn">More info</div>
  </div>
</section>

<section class="how">
  <div class="section-title" style="top:74px;color:#fff">How it Works</div>
  <div class="underline" style="left:552px;top:121px;background:#6fc266"></div>

  <div class="step-box" style="left:248px;top:233px"><h4 style="left:47px">Discovery</h4><p>We learn about your business and goals.</p></div>
  <div class="step-ring" style="left:114px;top:199px"><div class="inner">
    <svg width="64" height="64" viewBox="0 0 64 64" fill="none" stroke="#222" stroke-width="2.5"><circle cx="26" cy="20" r="11"/><path d="M6 52c0-12 10-18 20-18"/><circle cx="42" cy="44" r="9"/><line x1="49" y1="51" x2="58" y2="60"/></svg>
  </div></div>
  <div class="step-num" style="left:124px;top:203px">1</div>

  <div class="step-box" style="left:754px;top:233px"><h4>Strategy</h4><p>Develop a custom lead-generation plan.</p></div>
  <div class="step-ring" style="left:619px;top:199px"><div class="inner">
    <svg width="64" height="64" viewBox="0 0 64 64" fill="none" stroke="#222" stroke-width="2.5"><rect x="12" y="44" width="40" height="8"/><rect x="20" y="24" width="24" height="20"/><line x1="32" y1="8" x2="32" y2="24"/><line x1="26" y1="14" x2="38" y2="14"/></svg>
  </div></div>
  <div class="step-num" style="left:624px;top:203px">2</div>

  <div class="step-box" style="left:248px;top:437px"><h4>Execution</h4><p>Launch campaigns and deliver high-quality leads.</p></div>
  <div class="step-ring" style="left:114px;top:403px"><div class="inner">
    <svg width="64" height="64" viewBox="0 0 64 64" fill="none" stroke="#222" stroke-width="2.5"><path d="M6 50h14l12 6 24-10"/><path d="M20 50l14-6h10"/><line x1="34" y1="36" x2="34" y2="8"/><path d="M26 16l8-8 8 8"/></svg>
  </div></div>
  <div class="step-num" style="left:126px;top:407px">3</div>

  <div class="step-box" style="left:754px;top:437px"><h4 style="left:45px">Optimization</h4><p style="left:45px">Continuously improve for sustained results.</p></div>
  <div class="step-ring" style="left:619px;top:403px"><div class="inner">
    <svg width="64" height="64" viewBox="0 0 64 64" fill="none" stroke="#222" stroke-width="2.5"><line x1="6" y1="56" x2="58" y2="56"/><rect x="12" y="40" width="7" height="16"/><rect x="24" y="32" width="7" height="24"/><rect x="36" y="24" width="7" height="32"/><polyline points="8,38 30,22 54,8"/><path d="M44 8h10v10"/></svg>
  </div></div>
  <div class="step-num" style="left:624px;top:407px">4</div>
</section>

<section class="why">
  <div class="abs why-art" role="img" aria-label="Illustration of a person with a laptop beside a large checklist clipboard and a rising green arrow"></div>
  <h2>Why Choose us</h2>
  <div class="underline" style="left:641px;top:2490px"></div>
  <div class="why-item" style="top:2527px">
    <svg width="36" height="34" viewBox="0 0 36 34"><path d="M2 18l10 12L34 2" fill="none" stroke="#2c74f6" stroke-width="4"/></svg>
    <h4>Performance-Based</h4><p>Only pay for the results we deliver.</p>
  </div>
  <div class="why-item" style="top:2633px">
    <svg width="36" height="34" viewBox="0 0 36 34"><path d="M2 18l10 12L34 2" fill="none" stroke="#2c74f6" stroke-width="4"/></svg>
    <h4>Comprehensive Services</h4><p>End-to-end solutions for all your lead generation needs.</p>
  </div>
  <div class="why-item" style="top:2737px">
    <svg width="36" height="34" viewBox="0 0 36 34"><path d="M2 18l10 12L34 2" fill="none" stroke="#2c74f6" stroke-width="4"/></svg>
    <h4>Proven Expertise</h4><p>Trusted by businesses across industries.</p>
  </div>
  <div class="btn" style="left:639px;top:2845px;width:223px;height:46px">Get Free Consultation</div>
</section>

<div class="divider" style="top:2938px"></div>

<section class="testimonials">
  <div class="section-title" style="top:2996px;font-weight:700">Testimonials</div>
  <div class="underline" style="left:552px;top:3044px"></div>
  <div class="t-card" style="left:168px">
    <div class="t-avatar" role="img" aria-label="Client portrait"></div>
    <p>Lorem ipsum dolor sit amet, consectetur adipiscing elit, sed do eiusmod tempor incididunt ut labore et dolore magna aliqua.</p>
    <div class="t-stars">★★★★★</div><div class="t-name">Mira Delacourt</div><div class="t-role">Sales Officer</div>
  </div>
  <div class="t-card" style="left:463px">
    <div class="t-avatar" role="img" aria-label="Client portrait"></div>
    <p>Lorem ipsum dolor sit amet, consectetur adipiscing elit, sed do eiusmod tempor incididunt ut labore et dolore magna aliqua.</p>
    <div class="t-stars">★★★★★</div><div class="t-name">Owen Castell</div><div class="t-role">Sales Officer</div>
  </div>
  <div class="t-card" style="left:754px">
    <div class="t-avatar" role="img" aria-label="Client portrait"></div>
    <p>Lorem ipsum dolor sit amet, consectetur adipiscing elit, sed do eiusmod tempor incididunt ut labore et dolore magna aliqua.</p>
    <div class="t-stars">★★★★★</div><div class="t-name">Mira Delacourt</div><div class="t-role">Sales Officer</div>
  </div>
</section>

<div class="partners">
  <span>Plinth</span><span>Corvel Academy</span><span>Talkwell</span><span>Norra</span><span>Lumen Path</span><span>Harbor Inn</span><span>Vextra</span>
</div>

<section class="contact">
  <h2>Contact us</h2>
  <p class="intro">Lorem ipsum dolor sit amet, consectetur adipiscing elit, sed do eiusmod tempor incididunt ut labore et dolore magna aliqua. Quis ipsum suspendisse ultrices gravida.</p>
  <div class="field-label" style="top:220px">Name:</div>
  <div class="field" style="top:248px"></div>
  <div class="field-label" style="top:304px">Email:</div>
  <div class="field" style="top:332px"></div>
  <div class="field-label" style="top:388px">Business Name:</div>
  <div class="field" style="top:416px"></div>
  <div class="field-label" style="top:472px">How can we help you?</div>
  <div class="field" style="top:498px;height:107px"></div>
  <div class="btn">Submit</div>
</section>

<footer>
  <div class="copy">Copyright 2025 Brightvane.xyz All Rights Reserved.</div>
  <div class="social" style="left:1020px" aria-label="Social link"></div>
  <div class="social" style="left:1054px" aria-label="Social link"></div>
  <div class="social" style="left:1087px" aria-label="Social link"></div>
</footer>

</body>
</html>
```